Double-sided business card needed - specific brief

We need a double sided business card designed for our company Radiant Trimline. Having lost a lot of weight myself, the back of the card needs to show my before and after pictures. It needs to cover the entire back side of the card. This might be with my two before pictures over set on top of my main after picture or in separate frames. I'll leave that to your artistic consideration. The front needs to have our logo with contact details centred below.

The cards will be printed by PRINTVEX.com and will be rectangular, 84mm x 55mm, but with ROUNDED edges. Please therefore present your designs rectangular but with rounded edges if possible.

The card should be designed in LANDSCAPE orientation.

As well as the logo, the front of the card should have the following details:

Carol Whitby
Weight Loss Motivator with 189lb personal loss
carol@radiant-trimline.example
+44 (0)7700 900418

The website is important so should perhaps be more bold than the rest:
www.radiant-trimline.example

My brand colours are: Pink #CD2366, Light Pink #FD88AD. Blue #1C9CB1, Light Blue #64C4DE

Target Market(s)

Women 30+

Contact Information for Business Card

As description above

Font styles to use
Sans Serif

Requirements
Must have
• Double sided.
• Back side entirely covered with my before and after pictures.
• You may wish to float my before pictures on top of my after picture or add them in different frames. I look forward to seeing your different suggestions.

```html
<!DOCTYPE html>
<html lang="en">
<head>
<meta charset="utf-8">
<title>Radiant Trimline – Business Card</title>
<link rel="stylesheet" href="https://fonts.googleapis.com/css2?family=Noto+Sans:wght@400;700&display=swap">
<style>
  :root {
    --pink: #CD2366;
    --light-pink: #FD88AD;
    --blue: #1C9CB1;
    --light-blue: #64C4DE;
    --white: #ffffff;
    --backdrop: #e9e4e6;
    --card-radius: 30px;
  }
  * { box-sizing: border-box; margin: 0; padding: 0; }
  html, body { width: 1200px; height: 856px; overflow: hidden; }
  body {
    background: var(--backdrop);
    font-family: "Noto Sans", sans-serif;
    position: relative;
  }
  .card {
    position: absolute;
    top: 251px;
    width: 540px;
    height: 354px;
    border-radius: var(--card-radius);
    overflow: hidden;
    box-shadow: 0 6px 18px rgba(0,0,0,0.12);
  }
  /* Front */
  .card-front { left: 40px; background: var(--white); }
  .brand {
    position: absolute; left: 30px; top: 38px;
    display: flex; align-items: center; gap: 6px;
    color: var(--pink); font-size: 11px; font-weight: 400;
  }
  .brand-dot {
    width: 14px; height: 14px; border-radius: 50%;
    background: var(--light-pink);
  }
  .contact {
    position: absolute; right: 28px; top: 22px;
    text-align: right; color: var(--pink);
    font-size: 9.5px; line-height: 1.45;
  }
  .identity {
    position: absolute; left: 0; right: 0; top: 132px;
    text-align: center; color: var(--pink);
  }
  .name-row {
    display: flex; align-items: center; justify-content: center; gap: 8px;
  }
  .rule { height: 2px; width: 105px; background: var(--pink); }
  .name { font-size: 23px; letter-spacing: 0.5px; }
  .tagline { font-size: 13px; margin-top: 2px; letter-spacing: 0.3px; }
  .web-band {
    position: absolute; left: 0; right: 0; bottom: 0; height: 52px;
    background: var(--pink); color: var(--white);
    display: flex; align-items: center; justify-content: center;
    font-size: 18px; font-weight: 700; letter-spacing: 0.5px;
  }
  /* Back */
  .card-back {
    left: 620px;
    background: linear-gradient(to bottom, var(--pink) 0 48%, var(--blue) 48% 100%);
  }
  .photo {
    position: absolute; border-radius: 50%;
    border: 2px solid rgba(255,255,255,0.6);
  }
  .photo-before-1 {
    left: 92px; top: 72px; width: 160px; height: 78px;
    background: radial-gradient(circle at 50% 45%, #d9a88a, #b9836c 60%, #e8ddd6);
  }
  .photo-before-2 {
    left: 370px; top: 20px; width: 150px; height: 82px;
    background: radial-gradient(circle at 50% 50%, #e8e3df, #8a7a5e 70%, #5f6b45);
  }
  .photo-after {
    left: 292px; top: 160px; width: 196px; height: 92px;
    background: radial-gradient(circle at 55% 45%, #3a4f7a, #7a5f44 55%, #c9b9a2);
  }
  .label-present {
    position: absolute; left: 498px; top: 196px;
    color: var(--light-pink); font-size: 12px;
    transform: translateX(-4px);
  }
</style>
</head>
<body>
  <section class="card card-front" aria-label="Business card front">
    <div class="brand"><span class="brand-dot"></span><span>Radiant Trimline</span></div>
    <div class="contact">
      <div>+44 (0)7700 900418</div>
      <div>carol@radiant-trimline.example</div>
    </div>
    <div class="identity">
      <div class="name-row">
        <span class="rule"></span>
        <span class="name">Carol Whitby</span>
        <span class="rule"></span>
      </div>
      <div class="tagline">Weight Loss Motivator with 189lb personal loss</div>
    </div>
    <div class="web-band">www.radiant-trimline.example</div>
  </section>

  <section class="card card-back" aria-label="Business card back">
    <div class="photo photo-before-1" role="img" aria-label="Before photo: Carol in a bridal veil"></div>
    <div class="photo photo-before-2" role="img" aria-label="Before photo: Carol outdoors holding a pet"></div>
    <div class="photo photo-after" role="img" aria-label="Present photo: Carol seated in a living room"></div>
    <span class="label-present">Present</span>
  </section>
</body>
</html>
```